web site update

I want to get a better website for a small high end remodeling and construction company
I currently have a web site but you will find that it is not good.
www.quenbrickhall.com
We are a high end construction / remodeling company that has been in business since 2003. We primarily work in the mid peninsula of the bay area. Most of our clientele are very educated captains of industry. This group is still the target client.
I had my logo designed by Mint Easel a few years ago and I do like it, I like the orange and black or orange a blue. I don’t have a lot of content on hand as far as professional photographs.
Number of pages not sure and are open to: design pages vs full function website
I think what I am after is a web presence that will seal the deal as we are getting high referrals from past clients.
Construction
1 page

```html
<!DOCTYPE html>
<html lang="en">
<head>
<meta charset="utf-8">
<title>Quenbrick Hall – Remodeling</title>
<link rel="stylesheet" href="https://fonts.googleapis.com/css2?family=Russo+One&family=Open+Sans:wght@400;600;700&family=Arimo:wght@400;700&display=swap">
<style>
:root{
  --orange:#ff5a00;
  --black:#111111;
  --ink:#1c1c1c;
  --text:#555555;
  --grey-bg:#efefef;
  --white:#ffffff;
  --footer:#121212;
  --footer-bottom:#000000;
  --footer-text:#cfa98b;
  --line:#9a9a9a;
}
*{margin:0;padding:0;box-sizing:border-box}
html,body{width:1200px;height:3158px;overflow:hidden}
body{position:relative;font-family:"Open Sans",Arial,sans-serif;color:var(--text);background:var(--white)}
.abs{position:absolute}
.heading{font-family:"Russo One",Arial,sans-serif;color:var(--black);letter-spacing:3px;text-align:center;width:100%;font-weight:400}

/* top bar */
.topbar{left:0;top:0;width:1200px;height:38px;background:var(--orange)}
.topbar p{position:absolute;left:61px;top:10px;font-size:14px;color:var(--white);font-weight:600}
.social-top{position:absolute;right:61px;top:8px;display:flex;gap:6px}
.social-top span{width:22px;height:22px;background:var(--black);display:block}

/* header */
.header{left:0;top:38px;width:1200px;height:120px;background:var(--white)}
.brand{position:absolute;left:64px;top:32px;display:flex;align-items:center;gap:12px}
.brand-square{width:48px;height:48px;background:var(--black)}
.brand-name{font-weight:700;font-size:19px;line-height:22px;color:var(--orange);letter-spacing:1px}
.nav{position:absolute;right:56px;top:44px;display:flex;align-items:center;font-family:"Arimo",Arial,sans-serif;font-size:16px;color:var(--ink)}
.nav a{text-decoration:none;color:var(--ink);padding:9px 12px}
.nav a.active{background:var(--black);color:var(--white);padding:9px 15px;margin-right:4px}

/* hero */
.hero{left:0;top:158px;width:1200px;height:522px;background:
  radial-gradient(ellipse 260px 300px at 230px 180px,rgba(190,220,245,.9),rgba(190,220,245,0) 70%),
  radial-gradient(ellipse 300px 200px at 980px 260px,rgba(245,200,140,.55),rgba(245,200,140,0) 70%),
  linear-gradient(100deg,#4f79aa 0%,#8fb2d3 18%,#d7c1a0 34%,#c89560 50%,#a9703f 68%,#7e5233 84%,#5c3a22 100%)}
.hero-box{position:absolute;left:61px;top:164px;width:463px;height:145px;background:rgba(30,30,30,.85)}
.hero-box h1{font-family:"Russo One",Arial,sans-serif;color:var(--white);font-size:37px;line-height:45px;letter-spacing:2px;padding:28px 0 0 28px;font-weight:400}
.hero-btn{position:absolute;left:61px;top:320px;width:135px;height:44px;background:var(--orange);color:var(--white);font-weight:700;font-size:15px;text-align:center;line-height:44px}
.dots{display:flex;gap:5px}
.dots i{width:12px;height:12px;border-radius:50%;background:var(--black);display:block}
.dots i.on{background:var(--orange)}
.hero .dots{position:absolute;left:612px;top:474px}

/* specialized */
.specialized{left:0;top:680px;width:1200px;height:693px;background:var(--grey-bg)}
.specialized .heading{position:absolute;top:76px;font-size:38px}
.lead{position:absolute;top:126px;left:0;width:100%;text-align:center;font-size:13px;line-height:22px;color:var(--text)}
.service{position:absolute;top:234px;width:303px;text-align:center}
.service .photo{width:303px;height:225px}
.service h3{margin-top:30px;font-weight:700;font-size:17px;letter-spacing:1.5px;color:var(--ink)}
.service p{margin-top:6px;font-size:12.5px;line-height:20px;color:var(--text)}
.btn{display:inline-block;margin-top:18px;width:99px;height:38px;line-height:38px;background:var(--orange);color:var(--white);font-size:14px;text-align:center}

/* provide */
.provide{left:0;top:1373px;width:1200px;height:743px;background:var(--white)}
.provide .heading{position:absolute;top:76px;font-size:38px}
.tabs{position:absolute;top:143px;left:0;width:100%;display:flex;justify-content:center;gap:24px;font-size:13px;color:var(--ink);letter-spacing:.5px}
.tabs span{padding:4px 10px;border-bottom:1px solid var(--line)}
.tabs span.on{background:var(--orange);color:var(--white);border-bottom-color:var(--orange);padding:4px 16px}
.tile{position:absolute;width:237px;height:190px}
.tile.feature{background:linear-gradient(160deg,#ff6a12,#f0651a 60%,#e8703a)}
.tile.feature h4{position:absolute;left:27px;top:20px;color:var(--white);font-size:17px;font-weight:700}
.tile.feature small{position:absolute;left:27px;top:45px;color:var(--white);font-size:14px}
.tile.feature span{position:absolute;left:23px;top:132px;border:2px solid var(--white);color:var(--white);font-weight:700;font-size:14px;padding:6px 10px}

/* testimonials */
.testimonials{left:0;top:2116px;width:1200px;height:505px;background:var(--grey-bg)}
.testimonials .heading{position:absolute;top:78px;font-size:38px}
.quote-mark{position:absolute;left:178px;top:40px;font-family:Georgia,serif;font-size:230px;line-height:230px;color:#d9d9d9}
.testimonials blockquote{position:absolute;top:160px;left:240px;width:720px;text-align:center;font-size:13px;line-height:24px;color:var(--text)}
.avatar{position:absolute;left:550px;top:236px;width:100px;height:100px;border-radius:50%;border:3px solid var(--orange);background:radial-gradient(circle at 50% 45%,#7a5843,#3b2b22 70%,#e9e4df)}
.person{position:absolute;top:356px;width:100%;text-align:center}
.person strong{display:block;font-size:20px;color:var(--ink);font-weight:700;letter-spacing:.5px}
.person small{display:block;margin-top:2px;font-size:12px;color:var(--text)}
.testimonials .dots{position:absolute;left:552px;top:424px}

/* partners */
.partners{left:0;top:2621px;width:1200px;height:158px;background:var(--white);display:flex;align-items:center;justify-content:center;gap:46px}
.partner{height:28px;background:#3a3a3a;border-radius:4px}
.partner.round{width:66px;height:66px;border-radius:50%}

/* footer */
.footer{left:0;top:2779px;width:1200px;height:341px;background:var(--footer)}
.footer h5{position:absolute;top:48px;color:var(--white);font-size:15px;font-weight:700;letter-spacing:.5px}
.about-text{position:absolute;left:61px;top:88px;width:260px;font-size:13.5px;line-height:21px;color:var(--footer-text)}
.foot-social{position:absolute;left:61px;top:244px;display:flex;gap:10px}
.foot-social span{width:29px;height:29px;border-radius:50%;background:#4a4a4a;display:block}
.contact-list{position:absolute;left:415px;top:92px;width:240px;list-style:none;font-size:12px;color:#d9d9d9;line-height:18px}
.contact-list li{display:flex;gap:10px;margin-bottom:14px}
.contact-list svg{flex:none;margin-top:1px}
.info-list{position:absolute;left:669px;top:96px;list-style:none;font-size:11.5px;color:#d9d9d9;text-transform:uppercase}
.info-list li{margin-bottom:17px}
.info-list li::before{content:">";color:var(--orange);margin-right:10px}
.news-text{position:absolute;left:888px;top:92px;width:250px;font-size:13.5px;line-height:27px;color:#8f8f8f}
.news-input{position:absolute;left:888px;top:183px;width:251px;height:48px;background:#191919;border:1px solid #2b2b2b;color:#bdbdbd;font-size:13px;padding:14px 16px}
.news-btn{position:absolute;left:888px;top:248px;width:251px;height:48px;background:var(--orange);color:var(--white);font-size:17px;text-align:center;line-height:48px}
.copyright{left:0;top:3120px;width:1200px;height:38px;background:var(--footer-bottom);color:var(--white);font-size:12px;text-align:center;line-height:38px}
</style>
</head>
<body>

<div class="abs topbar">
  <p>Welcome to Keystone Row, we have over 20 years of expertise</p>
  <div class="social-top"><span></span><span></span><span></span><span></span></div>
</div>

<header class="abs header">
  <div class="brand">
    <span class="brand-square"></span>
    <span class="brand-name">QUENBRICK<br>HALL</span>
  </div>
  <nav class="nav">
    <a class="active">Home</a><a>All properties</a><a>Shop</a><a>Services</a><a>About Us</a><a>Projects</a><a>FAQ</a><a>Contact</a>
  </nav>
</header>

<section class="abs hero" role="img" aria-label="Photo of a remodeled living room with wood furniture, wall niches and a view through tall windows">
  <div class="hero-box"><h1>WE MAKE DESIGN<br>REMODELING</h1></div>
  <div class="hero-btn">Learn More</div>
  <div class="dots"><i class="on"></i><i></i><i></i><i></i></div>
</section>

<section class="abs specialized">
  <h2 class="heading">WE ARE SPECIALIZED</h2>
  <p class="lead">Quenbrick Hall has a solid reputation for delivering exceptional architectural and interior design services to private sector,<br>and industrial clients.</p>
  <div class="service" style="left:61px">
    <div class="photo" role="img" aria-label="Photo of a bright white kitchen with bar stools" style="background:radial-gradient(ellipse 120px 70px at 150px 110px,#f4f1ea,rgba(244,241,234,0) 80%),linear-gradient(180deg,#cfcac2 0%,#9c968e 50%,#3e3a36 100%)"></div>
    <h3>ARCHITECTURAL PLANNING</h3>
    <p>Architecture is our passion, turning ideas into reali-<br>ty and giving buildings a timeless footprint<br>in a community are the values</p>
    <span class="btn">Read More</span>
  </div>
  <div class="service" style="left:444px">
    <div class="photo" role="img" aria-label="Photo of a sunlit room with a white armchair by the windows" style="background:radial-gradient(ellipse 90px 80px at 230px 100px,#eef1f2,rgba(238,241,242,0) 80%),linear-gradient(160deg,#b6ab9b,#7b705f 55%,#4a4238)"></div>
    <h3>DECORATION &amp; FURNITURE</h3>
    <p>Architecture is our passion, turning ideas into reali-<br>ty and giving buildings a timeless footprint<br>in a community are the values</p>
    <span class="btn">Read More</span>
  </div>
  <div class="service" style="left:838px">
    <div class="photo" role="img" aria-label="Photo of a cottage exterior with tall trees and garden" style="background:linear-gradient(180deg,#9a9c98 0%,#7d7a70 35%,#b49a7a 55%,#8c7258 75%,#4b4a3a 100%)"></div>
    <h3>LANDSCAPE DESIGN</h3>
    <p>Architecture is our passion, turning ideas into reali-<br>ty and giving buildings a timeless footprint<br>in a community are the values</p>
    <span class="btn">Read More</span>
  </div>
</section>

<section class="abs provide">
  <h2 class="heading">WE PROVIDE</h2>
  <div class="tabs"><span class="on">ALL</span><span>PROJECTS</span><span>HOUSES DECORATION</span><span>FURNITURE</span></div>
  <div class="tile" style="left:61px;top:237px;background:linear-gradient(180deg,#c3d0da 0%,#9aa9b4 40%,#a57c52 65%,#2c2823 100%)" role="img" aria-label="Photo of a kitchen with a view over the bay"></div>
  <div class="tile" style="left:341px;top:237px;background:linear-gradient(180deg,#b07a4c 0%,#d9c7b0 45%,#8a4a2c 70%,#4d2c1a 100%)" role="img" aria-label="Photo of a wood kitchen with tiled backsplash"></div>
  <div class="tile" style="left:621px;top:237px;background:linear-gradient(180deg,#e2dfda 0%,#c4beb5 40%,#4a3528 70%,#2a1f19 100%)" role="img" aria-label="Photo of a kitchen with pendant lights"></div>
  <div class="tile feature" style="left:905px;top:237px">
    <h4>Alder Court Residence</h4><small>Houses</small><span>Read More</span>
  </div>
  <div class="tile" style="left:61px;top:473px;background:linear-gradient(180deg,#d8dce4 0%,#9aa3c0 40%,#eef0f4 70%,#c9ccd4 100%)" role="img" aria-label="Photo of a bathroom counter with blue tiles"></div>
  <div class="tile" style="left:341px;top:473px;background:radial-gradient(ellipse 60px 60px at 190px 70px,#eef1f2,rgba(238,241,242,0) 80%),linear-gradient(160deg,#b6ab9b,#7b705f 55%,#4a4238)" role="img" aria-label="Photo of a room with an armchair by the windows"></div>
  <div class="tile" style="left:621px;top:473px;background:linear-gradient(180deg,#c9c5bd 0%,#a09a90 45%,#5b3b2a 75%,#3a2418 100%)" role="img" aria-label="Photo of an empty room with glass doors and wood floor"></div>
  <div class="tile" style="left:905px;top:473px;background:linear-gradient(180deg,#d8c9b3 0%,#b59e86 40%,#8e7a6a 70%,#5d4a3d 100%)" role="img" aria-label="Photo of a kitchen with a steel fridge"></div>
</section>

<section class="abs testimonials">
  <div class="quote-mark">“</div>
  <h2 class="heading">TESTIMONIALS</h2>
  <blockquote>Nounc at pretium est curabitur commodo&nbsp; leac est venenatis egestas sed aliquet augueveliit. Lorem ipsum dolor sit amet, consectetur adipiscing elit. Vivamus ac luctus liguia. Phasellus a ligula blandit.</blockquote>
  <div class="avatar" role="img" aria-label="Client portrait"></div>
  <div class="person"><strong>Daniel Oreton</strong><small>Site Builder</small></div>
  <div class="dots"><i class="on"></i><i></i><i></i><i></i><i></i></div>
</section>

<section class="abs partners" aria-label="Partners">
  <span class="partner" style="width:134px"></span>
  <span class="partner" style="width:104px"></span>
  <span class="partner round"></span>
  <span class="partner" style="width:100px"></span>
  <span class="partner" style="width:106px"></span>
  <span class="partner" style="width:124px"></span>
  <span class="partner round"></span>
</section>

<footer class="abs footer">
  <h5 style="left:61px">ABOUT US</h5>
  <p class="about-text">Ledgerline is a specialist property and finance company based in the American. The company provides a variety of custom-tailored finance solutions, risk retention group, captive and financial marketplaces.</p>
  <div class="foot-social"><span></span><span></span><span></span><span></span></div>

  <h5 style="left:415px">GET IN TOUCH</h5>
  <ul class="contact-list">
    <li><svg width="12" height="14" viewBox="0 0 12 14"><path d="M6 0a5 5 0 0 0-5 5c0 4 5 9 5 9s5-5 5-9a5 5 0 0 0-5-5zm0 7a2 2 0 1 1 0-4 2 2 0 0 1 0 4z" fill="#ff5a00"/></svg><span>2150 Alder Ave. Redwood Grove, CA 94000<br>United States</span></li>
    <li><svg width="13" height="13" viewBox="0 0 13 13"><path d="M3 0l2 3-1.5 1.5a8 8 0 0 0 5 5L10 8l3 2-1.5 3C6 13 0 7 0 1.5z" fill="#ff5a00"/></svg><span>(555) 014-2770</span></li>
    <li><svg width="13" height="13" viewBox="0 0 13 13"><path d="M0 6l13-6-6 13-1-6z" fill="#ff5a00"/></svg><span>info@quenbrickhall.com</span></li>
    <li><svg width="10" height="14" viewBox="0 0 10 14"><rect x="0.8" y="0.8" width="8.4" height="12.4" rx="1.5" fill="none" stroke="#ff5a00" stroke-width="1.6"/><circle cx="5" cy="11" r="1" fill="#ff5a00"/></svg><span>(555) 014-2770</span></li>
    <li><svg width="13" height="13" viewBox="0 0 13 13"><circle cx="6.5" cy="6.5" r="5.7" fill="none" stroke="#ff5a00" stroke-width="1.6"/><path d="M6.5 3v4h3" fill="none" stroke="#ff5a00" stroke-width="1.6"/></svg><span>Mon – Sat: 9:00 – 18:00</span></li>
  </ul>

  <h5 style="left:669px">INFORMATION</h5>
  <ul class="info-list">
    <li>History of Elmsbury</li>
    <li>Harbor Street Food</li>
    <li>The Mist of Vellmoor</li>
    <li>Stone &amp; Timber Notes</li>
    <li>Coastal Road Trip</li>
    <li>The Quiet – Cedar</li>
  </ul>

  <h5 style="left:888px">NEWS LETTER</h5>
  <p class="news-text">Enter your email address for our mailing list to keep yourself up to date with our latest news.</p>
  <div class="news-input">Email</div>
  <div class="news-btn">Submit</div>
</footer>

<div class="abs copyright">© 2016 Quenbrick Hall. All Rights Reserved.</div>

</body>
</html>
```